Varrow Property Group Business cards

I am starting a property development and consultancy business called Varrow Property Group. I have a logo designed and a website on its way:
www.varrowgroup-example.com.au

I need a business card with the following:

Front:
Mostly orange with logo taking up all front of card

Back of card:
Logo

Miles Harcourt
Managing Director

T +61 455 207 364
E miles.harcourt@varrowgroup-example.com.au
www.varrowgroup-example.com.au

Industry/Entity Type

Business

Requirements
Must have
• curved edges

```html
<!DOCTYPE html>
<html lang="en">
<head>
<meta charset="utf-8">
<title>Varrow Property Group – Business Cards</title>
<link rel="stylesheet" href="https://fonts.googleapis.com/css2?family=Questrial&display=swap">
<style>
  :root {
    --orange: #f9ab1e;
    --white: #ffffff;
    --ink: #3a3a3a;
    --label: #9a9a9a;
    --backdrop: #cfcfd1;
    --card-shadow: rgba(0, 0, 0, 0.18);
  }
  * { box-sizing: border-box; margin: 0; padding: 0; }
  html, body {
    width: 1200px;
    height: 1000px;
    overflow: hidden;
  }
  body {
    position: relative;
    background: var(--backdrop);
    font-family: "Questrial", "Century Gothic", sans-serif;
    color: var(--ink);
  }
  .card {
    position: absolute;
    width: 640px;
    height: 366px;
    background: var(--white);
    border-radius: 34px;
    overflow: hidden;
    box-shadow: 0 8px 22px var(--card-shadow);
  }

  /* Front */
  .card-front { left: 520px; top: 50px; }
  .card-front .front-field {
    position: absolute;
    left: 0; top: 0;
    width: 100%;
    height: 228px;
    background: var(--orange);
  }
  .card-front .brand-name {
    position: absolute;
    left: 40px;
    right: 40px;
    top: 34px;
    color: var(--white);
    font-weight: 400;
    text-transform: uppercase;
    line-height: 1;
  }
  .card-front .brand-name .brand-main {
    display: block;
    font-size: 128px;
    letter-spacing: 6px;
  }
  .card-front .brand-name .brand-sub {
    display: block;
    margin-top: 12px;
    font-size: 34px;
    letter-spacing: 9px;
  }

  /* Back */
  .card-back { left: 40px; top: 480px; }
  .card-back .back-band {
    position: absolute;
    left: 0; top: 28px;
    width: 100%;
    height: 110px;
    background: var(--orange);
  }
  .card-back .brand-name {
    position: absolute;
    right: 34px;
    top: 46px;
    color: var(--white);
    text-transform: uppercase;
    text-align: right;
    line-height: 1;
  }
  .card-back .brand-name .brand-main {
    display: block;
    font-size: 58px;
    letter-spacing: 3px;
  }
  .card-back .brand-name .brand-sub {
    display: block;
    margin-top: 6px;
    font-size: 15px;
    letter-spacing: 5px;
  }
  .card-back .holder {
    position: absolute;
    left: 40px;
    top: 176px;
    font-size: 24px;
    white-space: nowrap;
  }
  .card-back .holder-name {
    text-transform: uppercase;
    letter-spacing: 0.5px;
    -webkit-text-stroke: 0.9px var(--ink);
  }
  .card-back .contact-list {
    position: absolute;
    left: 40px;
    top: 222px;
    list-style: none;
    font-size: 21px;
    line-height: 32px;
  }
  .card-back .contact-list .label {
    display: inline-block;
    width: 30px;
    color: var(--label);
  }
</style>
</head>
<body>

  <section class="card card-front" aria-label="Business card front">
    <div class="front-field"></div>
    <h1 class="brand-name">
      <span class="brand-main">Varrow</span>
      <span class="brand-sub">Property Group</span>
    </h1>
  </section>

  <section class="card card-back" aria-label="Business card back">
    <div class="back-band"></div>
    <p class="brand-name">
      <span class="brand-main">Varrow</span>
      <span class="brand-sub">Property Group</span>
    </p>
    <p class="holder">
      <span class="holder-name">Miles Harcourt</span>
      <span class="holder-role">Managing Director</span>
    </p>
    <ul class="contact-list">
      <li><span class="label">t.</span>+61 455 207 364</li>
      <li><span class="label">e.</span>miles.harcourt@varrowgroup-example.com.au</li>
      <li><span class="label">w.</span>varrowgroup-example.com.au</li>
    </ul>
  </section>

</body>
</html>
```